Stationery using new logo for pharmacy and gift shop

We need a letterhead, business card, gift voucher and possibly compliments slip design for our pharmacy and gift shop using our new logo.
The letterhead would need to be produced in both colour (purple and green) and grayscale and the business card would preferably be one-sided, but can be two-sided if this works better with the information it needs to have on it.

We would like a simple and elegant design, but not so simple that it looks like we've done it ourselves on Word. Use of our colours would be great but the letterhead would need to look good if printed on our black and white laser printer. If this is not possible then an additional version for grayscale would be needed.

We would need to receive high quality files that we can work with easily, such as pdf's for the letterhead that we can print instantly or order online as it appears on screen and business cards in jpeg and pdf so we can upload to printing sites.
We would like the vouchers in denominations of £5 and £10 in A5 size in a printable format such as PDF so that we don't have to resize.

Letterhead is for use in correspondence and invoicing to patients, surgeries, traders, customers etc.

Our preferred font is Orkney

Letterhead Info
Address
47 Fenwick Rd.
Ashby Fells
Westmoor
CA21 4QT

Tel: (01632) 960417
Fax: (01632) 960538
Website: www.brantleyspharmacy.example
Email: patientcare@brantleyspharmacy.example

Business Card Info.
As above but email address is: rkdbrantley@mailbox.example

Voucher Info.
Small print to state that any change will be paid as a credit note.
Space for a staff member to sign, date and stamp voucher

I have quite a few logo files so please ask if you need more uploaded. Or if you need more information to improve the design then please contact me.

Target Market(s)

Both retail customers and professional colleagues

Industry/Entity Type

Pharmacy

Font styles to use
Other font styles liked:
• orkney

Colors
ffffff
9bcb3c
6b449b

Requirements
Must have
• Must be clear and legible with a professional feel. Must use the logo well and all aspects of the designs should work well together.
• Final files MUST be easy to use for non-computer specialists. I need staff to be able to pull up a letterhead template easily if they are writing a letter or raising an invoice. The business card must be in a format ready to be sent to print.
Nice to have
• Letterhead available in a word processor program like word so that letters can be sent by email as well as print or print and scan.

```html
<!DOCTYPE html>
<html lang="en">
<head>
<meta charset="utf-8">
<title>Brantleys Chemist – Stationery</title>
<link href="https://fonts.googleapis.com/css2?family=Questrial&family=Open+Sans:wght@400;600&family=Great+Vibes&display=swap" rel="stylesheet">
<style>
  :root {
    --purple: #6b449b;
    --green: #9bcb3c;
    --white: #ffffff;
    --paper-edge: #d9dce6;
    --ink: #2b2b2b;
    --backdrop: #e4e8f2;
  }
  * { box-sizing: border-box; margin: 0; padding: 0; }
  html, body { width: 1200px; height: 1026px; overflow: hidden; }
  body { background: var(--backdrop); position: relative; font-family: "Open Sans", sans-serif; color: var(--ink); }

  .sheet { position: absolute; background: var(--white); border: 1px solid var(--paper-edge); overflow: hidden; }
  .sheet--purple { background: var(--purple); border-color: var(--purple); }

  .brand { position: absolute; display: flex; align-items: center; gap: 4px; font-family: "Questrial", sans-serif; color: var(--purple); white-space: nowrap; letter-spacing: 0.02em; }
  .brand__square { display: block; background: var(--purple); }
  .brand--light { color: var(--white); }
  .brand--light .brand__square { background: var(--white); }

  .letter-body { position: absolute; font-size: 4.7px; line-height: 1.26; text-align: justify; }
  .letter-body p { margin-bottom: 5px; }

  .footer-contact { position: absolute; left: 0; right: 0; text-align: center; font-size: 3.6px; line-height: 1.45; }
  .footer-bar { position: absolute; left: 0; right: 0; bottom: 0; height: 3px; display: flex; }
  .footer-bar__purple { flex: 0 0 75%; background: var(--purple); }
  .footer-bar__green { flex: 1; background: var(--green); }

  .slip-contact { position: absolute; font-size: 3.6px; line-height: 1.45; }
  .slip-greeting { position: absolute; font-family: "Great Vibes", cursive; color: var(--purple); font-size: 17px; }

  .envelope-flap { position: absolute; left: 0; top: 0; }

  .folder-contact { position: absolute; left: 0; right: 0; bottom: 17px; text-align: center; color: var(--white); font-size: 5px; line-height: 1.5; }

  .card-front .brand { left: 0; right: 0; top: 26px; justify-content: center; font-size: 6.5px; }
  .card-back__name { position: absolute; left: 8px; top: 41px; font-size: 3.6px; font-weight: 600; color: var(--purple); }
  .card-back__role { position: absolute; left: 8px; top: 46px; font-size: 2.6px; }
  .card-back__address { position: absolute; left: 8px; top: 50px; font-size: 2.6px; line-height: 1.3; }
  .card-back__divider { position: absolute; left: 70px; top: 41px; width: 1px; height: 15px; background: var(--green); }
  .card-back__details { position: absolute; left: 73px; top: 41px; width: 42px; font-size: 2.4px; line-height: 1.35; white-space: nowrap; }

  .showcase-brand { position: absolute; left: 853px; top: 785px; width: 190px; justify-content: center; font-size: 19px; gap: 8px; }
</style>
</head>
<body>

  <!-- Letterhead, folded -->
  <section class="sheet letterhead" style="left:136px; top:99px; width:270px; height:381px;">
    <div class="brand" style="left:22px; top:22px; font-size:7px;"><span class="brand__square" style="width:13px;height:13px;"></span>BRANTLEYS CHEMIST</div>
    <div class="letter-body" style="left:22px; top:80px; width:226px;">
      <p>Thank you for choosing our pharmacy for your prescriptions and everyday health needs. This letter confirms the details of your recent request and sets out the next steps we will take on your behalf. Please keep it safe with your records and contact us if anything looks incorrect or has changed since your last visit. We have reviewed your repeat prescription with your surgery and your regular medicines have been approved for the coming three months. Any new items added by your doctor will be explained by one of our pharmacists when you collect them, and we are happy to talk through dosage, timing and any side effects you may notice. If you take several medicines each day, we can supply them in a weekly dosette box to make things simpler at home. For patients who find it difficult to visit the shop, our free delivery service runs every weekday afternoon across the town and surrounding villages. Simply let us know a convenient time and a member of our team will bring your order to your door. We also offer flu vaccinations, blood pressure checks and medicine reviews by appointment in our private consultation room.</p>
      <p>Your repeat medication will be ready for collection within three working days of your request. If you would prefer home delivery, our team can arrange this at no extra cost for eligible patients living nearby. Please remember to bring your exemption card or prepayment certificate with you, as we are required to check it before handing over any prescription items. If your circumstances change, just let us know at the counter and we will update your record straight away.</p>
      <p>We also stock a wide range of greeting cards, toiletries, fragrances and gifts in store, so do take a moment to browse on your next visit. Whether you are looking for a birthday present, a thank you gift or a small treat for yourself, our staff are always happy to help you find something special. Gift vouchers are available in five and ten pound values and can be spent on any item in our gift range throughout the year.</p>
      <p>Should you have any questions about your treatment, please speak to one of our pharmacists in confidence, either in person or by telephone during opening hours. We value your feedback and use it to improve the service we provide to every patient and customer. Thank you once again for your continued custom. We look forward to seeing you again soon.</p>
    </div>
    <div class="footer-contact" style="bottom:12px;">
      47 Fenwick Rd. Ashby Fells Westmoor CA21 4QT<br>
      Tel: (01632) 960417 &nbsp;|&nbsp; Fax: (01632) 960538 &nbsp;|&nbsp; Email: patientcare@brantleyspharmacy.example<br>
      Website: www.brantleyspharmacy.example
    </div>
    <div class="footer-bar"><span class="footer-bar__purple"></span><span class="footer-bar__green"></span></div>
  </section>

  <!-- Compliments slip, top -->
  <section class="sheet compliments-slip" style="left:465px; top:163px; width:283px; height:141px;">
    <div class="brand" style="left:13px; top:18px; font-size:9px;"><span class="brand__square" style="width:18px;height:18px;"></span>BRANTLEYS CHEMIST</div>
    <div class="slip-contact" style="left:14px; top:114px;">
      47 Fenwick Rd. Ashby Fells Westmoor CA21 4QT<br>
      Tel: (01632) 960417 &nbsp;|&nbsp; Fax: (01632) 960538<br>
      Website: www.brantleyspharmacy.example
    </div>
  </section>

  <!-- Envelope -->
  <section class="sheet envelope" style="left:765px; top:162px; width:281px; height:140px;">
    <svg class="envelope-flap" width="281" height="42" viewBox="0 0 281 42" aria-hidden="true">
      <polygon points="0,0 281,0 264,42 17,42" fill="var(--purple)"/>
    </svg>
  </section>

  <!-- Letterhead, flat -->
  <section class="sheet letterhead" style="left:472px; top:364px; width:272px; height:382px;">
    <div class="brand" style="left:21px; top:22px; font-size:7px;"><span class="brand__square" style="width:13px;height:13px;"></span>BRANTLEYS CHEMIST</div>
    <div class="letter-body" style="left:22px; top:79px; width:228px;">
      <p>Thank you for choosing our pharmacy for your prescriptions and everyday health needs. This letter confirms the details of your recent request and sets out the next steps we will take on your behalf. Please keep it safe with your records and contact us if anything looks incorrect or has changed since your last visit. We have reviewed your repeat prescription with your surgery and your regular medicines have been approved for the coming three months. Any new items added by your doctor will be explained by one of our pharmacists when you collect them, and we are happy to talk through dosage, timing and any side effects you may notice. If you take several medicines each day, we can supply them in a weekly dosette box to make things simpler at home. For patients who find it difficult to visit the shop, our free delivery service runs every weekday afternoon across the town and surrounding villages. Simply let us know a convenient time and a member of our team will bring your order to your door. We also offer flu vaccinations, blood pressure checks and medicine reviews by appointment in our private consultation room.</p>
      <p>Your repeat medication will be ready for collection within three working days of your request. If you would prefer home delivery, our team can arrange this at no extra cost for eligible patients living nearby. Please remember to bring your exemption card or prepayment certificate with you, as we are required to check it before handing over any prescription items. If your circumstances change, just let us know at the counter and we will update your record straight away.</p>
      <p>We also stock a wide range of greeting cards, toiletries, fragrances and gifts in store, so do take a moment to browse on your next visit. Whether you are looking for a birthday present, a thank you gift or a small treat for yourself, our staff are always happy to help you find something special. Gift vouchers are available in five and ten pound values and can be spent on any item in our gift range throughout the year.</p>
      <p>Should you have any questions about your treatment, please speak to one of our pharmacists in confidence, either in person or by telephone during opening hours. We value your feedback and use it to improve the service we provide to every patient and customer. Thank you once again for your continued custom. We look forward to seeing you again soon.</p>
    </div>
    <div class="footer-contact" style="bottom:12px;">
      47 Fenwick Rd. Ashby Fells Westmoor CA21 4QT<br>
      Tel: (01632) 960417 &nbsp;|&nbsp; Fax: (01632) 960538 &nbsp;|&nbsp; Email: patientcare@brantleyspharmacy.example<br>
      Website: www.brantleyspharmacy.example
    </div>
    <div class="footer-bar"><span class="footer-bar__purple"></span><span class="footer-bar__green"></span></div>
  </section>

  <!-- Business card, front -->
  <section class="sheet sheet--purple card-front" style="left:917px; top:384px; width:117px; height:64px;">
    <div class="brand brand--light"><span class="brand__square" style="width:7px;height:7px;"></span>BRANTLEYS CHEMIST</div>
  </section>

  <!-- Business card, back -->
  <section class="sheet card-back" style="left:918px; top:489px; width:117px; height:64px;">
    <div class="brand" style="left:7px; top:7px; font-size:4.6px;"><span class="brand__square" style="width:8px;height:8px;"></span>BRANTLEYS CHEMIST</div>
    <div class="card-back__name">DANIEL HURST</div>
    <div class="card-back__role">Pharmacist</div>
    <div class="card-back__address">47 Fenwick Rd. Ashby Fells<br>Westmoor CA21 4QT</div>
    <div class="card-back__divider"></div>
    <div class="card-back__details">T: (01632) 960417<br>F: (01632) 960538<br>rkdbrantley@mailbox.example<br>www.brantleyspharmacy.example</div>
    <div class="footer-bar" style="height:2px;"><span class="footer-bar__purple"></span><span class="footer-bar__green"></span></div>
  </section>

  <!-- Presentation folder -->
  <section class="sheet sheet--purple folder" style="left:89px; top:535px; width:322px; height:405px;">
    <div class="brand brand--light" style="left:94px; top:33px; font-size:12px; gap:7px;"><span class="brand__square" style="width:27px;height:27px;"></span>BRANTLEYS CHEMIST</div>
    <div class="folder-contact">
      47 Fenwick Rd. Ashby Fells Westmoor CA21 4QT &nbsp;|&nbsp; Tel: (01632) 960417 &nbsp;|&nbsp; Fax: (01632) 960538<br>
      Website: www.brantleyspharmacy.example
    </div>
  </section>

  <!-- Compliments slip, bottom -->
  <section class="sheet compliments-slip" style="left:474px; top:796px; width:270px; height:127px;">
    <div class="brand" style="left:11px; top:12px; font-size:8px;"><span class="brand__square" style="width:17px;height:17px;"></span>BRANTLEYS CHEMIST</div>
    <div class="slip-greeting" style="left:158px; top:96px;">With Compliments</div>
  </section>

  <!-- Brand showcase -->
  <div class="brand showcase-brand"><span class="brand__square" style="width:20px;height:20px;"></span>BRANTLEYS CHEMIST</div>

</body>
</html>
```